Amazon Fly/Cruise Expedition Cruise Package.

Task Description
I am wanting to create a double sided A4 colour flyer (Finished size: 297 x 210mm) for a Fly/Cruise package from Australia to the Amazon.
The idea is that I would like the art work or design work done for the flyer that I can then send to a printer to do the printing of these flyers.

My business is a retail cruise travel agent that specializes in selling all-inclusive packages on luxury expedition ships and in this case I intend to promote this cruise to people that are interested in wildlife and also bird watching.

This link will show you the full brochure from the Tour Operator that we will be using to give you more information on them and the cruise we are travelling on.
https://www.orvatrips.com/expedition/amazon-voyage#overview
This is an American company and basically I am giving you there brochure to give you more information.

I do all the costing's from Australia and ask you ignore the costing's etc. in their brochure, it will however give you more information to work with.

I will also attach my logo so this can be included and a copy of the draft itinerary that I see as being the highlights however I am aware that we are limited on space and we need to get the key issues across and also as the trip is being marketed to bird watchers and wildlife enthusiasts then some good pictures of both the boat and a few good birds ones and let’s say a bird called a ????? and maybe a monkey.

We also need to show the costing's and what's included in the package.

And of course a call to action
All bookings and enquiries call Derek

1-300-419-873
WaveHarbor Pty Ltd
derek@waveharbor.com.au
PO Box 817
Kelton NSW 2031
Australia.

Target Market(s)

Travellers that are interested in Birds/Animals and Expedition cruising.

Colors

Designer to choose colors to be used in the design.

Requirements
Must have
• Easy to read
• Colour full
• 2 birds pics
• 1 photo of the boat
• waveharbor logo
Nice to have
• a crisp clean look and a professional appearance

```html
<!DOCTYPE html>
<html lang="en">
<head>
<meta charset="utf-8">
<title>Amazon Fly/Cruise Flyer – WaveHarbor</title>
<link href="https://fonts.googleapis.com/css2?family=Lato:wght@400;700;900&family=Raleway:wght@300&display=swap" rel="stylesheet">
<style>
:root{
  --stage:#232323;
  --navy:#1b2a63;
  --navy-deep:#121d4a;
  --gold:#f5d020;
  --red:#e3241b;
  --orange:#e2561c;
  --green:#0f3d12;
  --sand:#e7dd6a;
  --white:#ffffff;
  --ink:#1a1a1a;
  --blue-link:#1d3f95;
  --rust:#b5301a;
}
*{box-sizing:border-box;margin:0;padding:0}
html,body{width:1200px;height:871px;overflow:hidden;background:var(--stage);font-family:"Lato",sans-serif}
.canvas{position:relative;width:1200px;height:871px}
.page{position:absolute;top:47px;height:729px;overflow:hidden}
.page--front{left:58px;width:515px;background:var(--navy)}
.page--back{left:627px;top:49px;width:513px;height:725px;background:var(--sand)}
.side-label{position:absolute;top:806px;font-family:"Raleway",sans-serif;font-weight:300;font-size:33px;color:#fff;letter-spacing:1px}
.abs{position:absolute}
.brand{display:flex;align-items:center;gap:8px;font-weight:900;color:var(--navy);letter-spacing:.5px}
.brand__dot{width:26px;height:26px;border-radius:50%;background:var(--gold)}
/* front */
.hero{left:0;top:0;width:515px;height:340px;background:radial-gradient(ellipse at 50% 55%,#3b4a2a 0%,#1a2418 55%,#0b0f0b 100%)}
.title-art{left:95px;top:145px;width:300px;height:110px;border-radius:8px;background:linear-gradient(180deg,#f3d34a,#b98a10);opacity:.85}
.front-brand{left:0;top:26px;width:515px;justify-content:center;font-size:30px}
.intro{top:288px;width:515px;text-align:center;color:#fff;font-size:10px;line-height:12.5px}
.intro b{color:var(--gold);font-weight:700}
.day{left:24px;width:468px;color:#fff}
.day h2{color:var(--gold);font-size:12.5px;font-weight:900;margin-bottom:5px}
.day p{font-size:8.3px;line-height:10.4px;text-align:justify}
.fly{left:24px;top:525px;color:#fff;font-size:10px;font-weight:700}
.fly span{color:var(--gold)}
.band-red{left:0;top:546px;width:515px;height:24px;background:var(--red);color:var(--gold);font-weight:700;font-size:12.5px;display:flex;align-items:center;justify-content:center}
.watch{top:577px;width:515px;text-align:center;color:#fff;font-size:11px;line-height:14px}
.watch a{color:var(--gold);font-weight:700;text-decoration:none}
.strip{left:0;top:613px;width:515px;height:68px}
.band-yellow{left:0;top:687px;width:515px;height:42px;background:linear-gradient(180deg,#f7d61c,#e9b70c);display:flex;align-items:center;justify-content:center;font-weight:900;font-size:20px;color:var(--ink)}
/* back */
.back-head{left:0;top:0;width:513px;height:41px;background:var(--navy);color:var(--gold);font-weight:700;font-size:16px;display:flex;align-items:center;justify-content:center}
.ship-name{top:49px;width:513px;text-align:center;color:var(--red);font-weight:900;font-size:13px}
.copy{left:25px;width:465px;color:var(--ink);font-size:8.2px;line-height:10.4px;text-align:justify}
.copy p{margin-bottom:6px}
.copy b{font-weight:700}
.band-green{left:0;top:209px;width:513px;height:88px;background:var(--green);color:#fff;font-size:8.2px;line-height:10.4px}
.band-green h3{color:var(--gold);font-size:9.5px;font-weight:700;margin-bottom:4px}
.band-green p{margin-bottom:3px}
.col-l{left:25px;top:8px;width:230px}
.col-r{left:268px;top:8px;width:222px;text-align:justify}
.band-orange{left:0;top:297px;width:513px;height:23px;background:var(--orange);color:#fff;font-weight:700;font-size:10.5px;display:flex;align-items:center;justify-content:center}
.upgrades{top:328px}
.upgrades h3{font-size:9.5px;font-weight:700;margin-bottom:3px}
.upgrades p{margin-bottom:1.6px;text-align:left}
.jungle{left:0;top:395px;width:513px;height:240px;background:linear-gradient(180deg,var(--sand) 0%,#a9ab3a 45%,#6b7a2e 100%)}
.wildlife-head{top:399px;width:513px;text-align:center;font-weight:700;font-size:10px;color:var(--ink)}
.list{width:222px;font-size:8.6px;color:var(--blue-link);font-weight:700}
.list h4{color:var(--rust);font-size:8.8px;line-height:11px;font-weight:700;margin-bottom:2px}
.list li{list-style:none;padding-left:9px;position:relative;line-height:11px;margin-bottom:2.6px}
.list li::before{content:"";position:absolute;left:0;top:4px;width:4px;height:4px;border-radius:50%;background:var(--rust)}
.list li span{color:var(--ink);font-weight:400}
.list-l{left:36px;top:420px}
.list-r{left:297px;top:420px}
.bird{width:96px;height:96px;border-radius:50%;border:5px solid #3d4a1c;top:523px}
.back-brand{left:0;top:626px;width:513px;justify-content:center;font-size:24px}
.footer{left:0;top:669px;width:513px;height:56px;background:var(--navy);color:#fff}
.phone{left:40px;top:4px;font-size:26px;font-weight:900}
.web{left:44px;top:35px;font-size:9.5px;letter-spacing:3px}
.contact{left:276px;font-size:10.5px;font-weight:700;display:flex;align-items:center;gap:8px}
.ic{width:11px;height:11px;border-radius:50%;background:var(--gold);flex:none}
</style>
</head>
<body>
<div class="canvas">

  <section class="page page--front">
    <div class="abs hero" role="img" aria-label="Photo of a macaw and a toucan in the rainforest"></div>
    <div class="abs title-art" role="img" aria-label="Hand lettered gold title: a bird called Amazon"></div>
    <svg class="abs" style="left:0;top:0" width="515" height="729" viewBox="0 0 515 729" aria-hidden="true">
      <path d="M0 0H515V92Q257 148 0 92Z" fill="#fff"/>
      <path d="M0 330Q257 205 515 330V729H0Z" fill="var(--navy)"/>
      <path d="M0 330Q257 205 515 330" fill="none" stroke="#fff" stroke-width="5"/>
    </svg>
    <div class="abs brand front-brand"><span class="brand__dot"></span>WAVEHARBOR</div>

    <div class="abs intro"><b>Wed 15 April 2020 Fly from Australia to Lima</b><br>Transfer from the airport to the Miraflores Grand Hotel<br>Stay 15-18 Apr</div>

    <div class="abs day" style="top:332px">
      <h2>16 APRIL</h2>
      <p>This morning tour the historic district of Lima. Visit the cathedral, where Francisco Pizarro is entombed, the Plaza de Armas, the monastery and vast catacombs of the Iglesia de San Francisco before visiting Casa Morales, a private home dating back to the Conquistadors. This afternoon we enjoy lunch overlooking the pyramid, Huaca Pucllana. A terwards, we tour the ruins built by a Pre-Incan indigenous coastal civilization. Late this afternoon, we return to the hotel. This evening, enjoy the night in Lima on your own. Consider using this evening to experience some of Lima's world famous cuisine. (B,L)</p>
    </div>
    <div class="abs day" style="top:413px">
      <h2>17 APRIL</h2>
      <p>Today we begin with a visit to the vibrant Indian Market where crafters display a wide variety of handmade items, jewelry, and art. We have lunch at a local restaurant and explore the surrounding shops before returning to the hotel to refresh before a late afternoon visit to the Casa Vieja Museum. This museum is housed in an 18th century vice-royal mansion built over a 7thcentury pre-Columbian pyramid and surrounded by beautiful gardens. The museum was founded in 1926 and has the finest gold and silver collection from Ancient Peru. The galleries provide an overview of 3000 years of development of Peruvian pre- Columbian history. After our visit, we enjoy dinner at the museum's restaurant, Museo Casa Vieja, noted as one of Lima's finest dining options. We return to the hotel this evening and prepare for the next mornings' flight to Iquitos where we will connect with our (BLD)</p>
    </div>
    <div class="abs fly"><span>18 APRIL</span> WE FLY FROM LIMA TO IQUITOS</div>
    <div class="abs band-red">Amazon Cruise package starts on the Marisol 18 April – 25 April 2020.</div>
    <div class="abs watch">Watch this Link :<br><a href="https://www.orvatrips.com/expedition/amazon-voyage#overview">https://www.orvatrips.com/expedition/amazon-voyage#overview</a></div>
    <svg class="abs strip" width="515" height="68" viewBox="0 0 515 68" role="img" aria-label="Strip of wildlife photos: monkey, tanager, capybaras, egrets">
      <path d="M0 0H128L118 68H0Z" fill="#5d7a3a"/>
      <path d="M134 0H265L255 68H124Z" fill="#3f6a54"/>
      <path d="M271 0H402L392 68H261Z" fill="#6b4f34"/>
      <path d="M408 0H515V68H398Z" fill="#3d6b2c"/>
    </svg>
    <div class="abs band-yellow">All bookings and enquiries call Derek</div>
  </section>

  <section class="page page--back">
    <div class="abs jungle" role="img" aria-label="Faded rainforest photo background"></div>
    <div class="abs back-head">18-25 APRIL WE CRUISE IN UPPER DECK CABINS ON OUR SHIP</div>
    <div class="abs ship-name">THE MARISOL</div>
    <div class="abs copy" style="top:74px">
      <p>Travel aboard the Marisol, a luxurious vessel we have chartered for your adventure, which blends stylish design and modern comforts. Classic touches include magnificent floor-to-ceiling windows and — for those on the Upper Deck — private balconies. A ship staff and crew of 25, including a cruise director and local naturalist guides, are joined by an OT Expedition Leader &amp; Martin and Derek to ensure an unprecedented level of service. All 19 spacious suites are air-conditioned and feature en-suite bathrooms, a desk and ample closet space.</p>
      <p>We will be travelling in the High Water season this will allow us to go deeper into the Amazon Basin and further into the forest on our excursion boats we can also go into smaller tributaries- we will I hope see more wildlife and Birds that shun the main course of the river.</p>
      <p><b>Then insert as much of the day to day itinerary that you can.</b></p>
      <p><b>25 April we fly from Iquitos to Lima where we connect with our flight back to Australia and arrive back in Sydney on the 27th Aprilor you may wish to extend your trip.</b></p>
    </div>

    <div class="abs band-green">
      <div class="abs col-l">
        <h3>Suggested Extension:</h3>
        <p><b>Machu Picchu &amp; Cusco Extension 25 April – 01 May 2020</b></p>
        <p><b>6 night package- more details on request.</b></p>
        <p><b>AUD $6500 p/p twin /AUD $8100 solo.</b></p>
        <p>Or you a free to request any other options and I will put together a costing and itinerary for you.</p>
      </div>
      <div class="abs col-r">
        <h3>Costing &amp; Inclusions:</h3>
        <p>Return Economy class airfares.</p>
        <p>Transfers and accommodation and touring as per the brochure (for a more detailed cruise itinerary please ask) All Taxes</p>
        <p>Escorted by Derek Hallam and Martin Roe – Lima back to Lima.</p>
      </div>
    </div>
    <div class="abs band-orange">Deposit of $4000 per person due 7 days after booking. Final payment due on the 16th Dec 2019.</div>

    <div class="abs copy upgrades">
      <h3>Upgrades:</h3>
      <p>Please ask for the cost to upgrade to Business Class airfare.</p>
      <p>Please ask for the cost to upgrade to a Suite on the Marisol</p>
      <p>Other information that we may be able to include.</p>
      <p>See the File amazonfile1 page 3 as it has a nice description of the Cruise you will see the page titled defining the Amazon</p>
    </div>

    <div class="abs wildlife-head">Birdlife and Wildlife that we may have the opportunity to see on our trip pending on weather conditions:a</div>
    <ul class="abs list list-l">
      <h4>The 10 Most Beautiful Birds of Amazon Rainforest Jungle</h4>
      <li>The Hyacinth Macaw. <span>This is considered as one of the most beautiful bird of Amazon Rainforest jungle.</span></li>
      <li>Blue Fronted Amazon. &nbsp;• Scarlet Macaws.</li>
      <li>Spectacled Owl. &nbsp;• Plum Throated Cotinga.</li>
      <li>Crimson Topaz. &nbsp;• Oropendolas.</li>
      <li>Amazon Kingfisher</li>
    </ul>
    <ul class="abs list list-r">
      <h4>Top 10 Wildlife to Spot in the Amazon</h4>
      <li>Giant River Otters</li>
      <li>Toucans. &nbsp;• Macaws.</li>
      <li>Black Caimans. &nbsp;• Capybaras.</li>
      <li>Pink River Dolphins. &nbsp;• Piranhas.</li>
      <li>Jaguars.</li>
    </ul>

    <svg class="abs" style="left:0;top:585px" width="513" height="90" viewBox="0 0 513 90" aria-hidden="true">
      <path d="M0 40Q256 -10 513 40V90H0Z" fill="#fff"/>
    </svg>
    <div class="abs bird" style="left:87px;background:radial-gradient(circle,#8a6a3a,#3b4a22)" role="img" aria-label="Photo of an Amazon kingfisher on a branch"></div>
    <div class="abs bird" style="left:207px;background:radial-gradient(circle,#e6e6e6,#6f8fb0)" role="img" aria-label="Photo of a blue kingfisher"></div>
    <div class="abs bird" style="left:327px;background:radial-gradient(circle,#2c4fa3,#2b4a1e)" role="img" aria-label="Photo of a hyacinth macaw"></div>
    <div class="abs brand back-brand"><span class="brand__dot" style="width:20px;height:20px"></span>WAVEHARBOR</div>

    <div class="abs footer">
      <div class="abs phone">1-300-419-873</div>
      <div class="abs web">www.waveharbor.com.au</div>
      <svg class="abs" style="left:18px;top:12px" width="12" height="12" viewBox="0 0 12 12" aria-hidden="true"><circle cx="6" cy="6" r="6" fill="var(--gold)"/><path d="M4 3.5l1.2 1.3-.7.8a4 4 0 0 0 1.9 1.9l.8-.7 1.3 1.2-.9.9C5.5 8.6 3.4 6.5 3.1 4.4z" fill="var(--navy)"/></svg>
      <svg class="abs" style="left:18px;top:35px" width="12" height="12" viewBox="0 0 12 12" aria-hidden="true"><circle cx="6" cy="6" r="5.5" fill="none" stroke="var(--gold)" stroke-width="1.2"/><path d="M1 6h10M6 1c2 2 2 8 0 10M6 1c-2 2-2 8 0 10" fill="none" stroke="var(--gold)" stroke-width=".9"/></svg>
      <div class="abs contact" style="top:11px"><svg width="11" height="12" viewBox="0 0 11 12" aria-hidden="true"><path d="M5.5 0A4.5 4.5 0 0 0 1 4.5C1 8 5.5 12 5.5 12S10 8 10 4.5A4.5 4.5 0 0 0 5.5 0z" fill="var(--gold)"/><circle cx="5.5" cy="4.5" r="1.7" fill="var(--navy)"/></svg>PO Box 817 Kelton NSW 2031, Australia.</div>
      <div class="abs contact" style="top:30px"><span class="ic"></span>derek@waveharbor.com.au</div>
    </div>
  </section>

  <div class="side-label" style="left:275px">FRONT</div>
  <div class="side-label" style="left:851px">BACK</div>
</div>
</body>
</html>
```